Ferro Lanes - explore habits of productive people

Ferro Lanes is a social place around habits and productivity

The full brief below:

https://files.quorvanta.com/sheet/d/7Kp-RwTZMX2uqEebH-Y-cNdt4TgsWmFkyQoPJhwbrzVe/view?mode=viewer

Colors

Designer to choose colors to be used in the design.

Requirements
Must have
• - a feed page to display habits
• - a habit page to add a habit
• / clean, no cluttered design, lots of white space
• / inspired by material design or other design system
Nice to have
• - user page

```html
<!DOCTYPE html>
<html lang="en">
<head>
<meta charset="utf-8">
<title>Ferro Lanes – Feed</title>
<link href="https://fonts.googleapis.com/css2?family=Roboto:wght@400;500;700&family=Open+Sans:wght@400&display=swap" rel="stylesheet">
<style>
  :root{
    --bg:#f0f0f0;
    --surface:#ffffff;
    --ink:#111111;
    --text:#333333;
    --muted:#777777;
    --accent:#1a9bf0;
    --divider:#e6e6e6;
    --icon:#666666;
    --photo-a:#3ccfe8;
    --photo-b:#e8ecef;
    --photo-c:#5b95d6;
  }
  *{box-sizing:border-box;margin:0;padding:0}
  html,body{width:1179px;height:1200px;overflow:hidden}
  body{background:var(--bg);font-family:"Roboto",Arial,sans-serif;color:var(--text);position:relative}
  .topbar{position:absolute;left:0;top:0;width:1179px;height:75px;background:var(--surface)}
  .brand{position:absolute;left:109px;top:20px;font-size:28px;font-weight:700;color:var(--ink);letter-spacing:-0.5px}
  .user{position:absolute;left:886px;top:25px;font-size:16px;color:var(--ink)}
  .user-avatar{position:absolute;left:979px;top:16px;width:38px;height:38px;border-radius:50%;background:linear-gradient(135deg,#8a5a3c,#3b2418);box-shadow:0 0 0 3px #fff,0 1px 4px rgba(0,0,0,.25)}
  .add-btn{position:absolute;left:1031px;top:16px;width:38px;height:38px;border-radius:50%;background:var(--accent);color:#fff;font-size:22px;line-height:36px;text-align:center;box-shadow:0 2px 5px rgba(0,0,0,.2)}
  .page-title{position:absolute;left:178px;top:121px;font-size:20px;color:#666;font-weight:400}
  .post{position:absolute;left:173px;width:833px;background:var(--surface);box-shadow:0 1px 3px rgba(0,0,0,.06)}
  .avatar{position:absolute;left:29px;top:26px;width:56px;height:56px;border-radius:50%;background:linear-gradient(135deg,#b57a55,#4a2c1e);box-shadow:0 0 0 3px #fff,0 1px 5px rgba(0,0,0,.25)}
  .avatar.light{background:linear-gradient(135deg,#d9a98a,#3a2a24)}
  .author{position:absolute;left:129px;top:24px;font-size:17px;font-weight:500;color:var(--accent)}
  .meta{position:absolute;left:129px;top:50px;font-size:12px;color:var(--muted);display:flex;align-items:center;gap:12px}
  .meta .dot{width:3px;height:3px;border-radius:50%;background:var(--muted)}
  .body{position:absolute;left:129px;top:78px;font-size:13.5px;color:var(--text)}
  .actions{position:absolute;display:flex;align-items:center;gap:20px;font-size:12px;font-weight:700;color:var(--accent)}
  .action{display:flex;align-items:center;gap:11px}
  .action svg{width:17px;height:17px}
  .divider{position:absolute;left:10px;right:10px;height:1px;background:var(--divider)}
  .comment{position:absolute;left:30px;font-size:12.5px;color:#555}
  .tools{position:absolute;right:32px;display:flex;gap:16px}
  .tools svg{width:13px;height:13px}
  .photo{position:absolute;left:-2px;top:121px;width:835px;height:232px;background:linear-gradient(90deg,var(--photo-a) 0%,var(--photo-a) 35%,var(--photo-b) 55%,var(--photo-b) 72%,var(--photo-c) 72%,var(--photo-c) 100%)}
  .footer{position:absolute;left:0;top:1138px;width:1179px;height:62px;background:var(--surface)}
  .footer-text{position:absolute;left:112px;top:23px;font-family:"Open Sans",Arial,sans-serif;font-size:14px;color:#222;display:flex;align-items:center;gap:8px}
</style>
</head>
<body>
  <header class="topbar">
    <div class="brand">Ferro Lanes</div>
    <div class="user">Orin Vale</div>
    <div class="user-avatar" role="img" aria-label="Profile photo of the signed-in user"></div>
    <div class="add-btn">+</div>
  </header>

  <h1 class="page-title">Feed</h1>

  <article class="post" style="top:165px;height:199px">
    <div class="avatar" role="img" aria-label="Profile photo of Marisol"></div>
    <div class="author">Marisol</div>
    <div class="meta"><span>3 hours ago</span><span class="dot"></span><span>Message sent today lorium ipsum</span></div>
    <p class="body">After I pour my morning cup of coffee, I will meditate for sixty seconds.</p>
    <div class="actions" style="left:129px;top:115px">
      <span class="action"><svg viewBox="0 0 20 20" fill="none" stroke="currentColor" stroke-width="1.3"><path d="M6 10V4a1 1 0 012 0v5M8 9V2.5a1 1 0 012 0V9M10 9V3a1 1 0 012 0v6M12 9V5a1 1 0 012 0v7c0 4-2 6-5 6s-4-1-6-5l-1-2a1 1 0 012-1l2 2"/></svg>250 high five</span>
      <span class="action"><svg viewBox="0 0 20 20" fill="none" stroke="currentColor" stroke-width="1.2"><rect x="2" y="3" width="16" height="11"/><path d="M5 6h10M5 8.5h10M5 11h7M12 14l2 3v-3"/></svg>85 Comments</span>
    </div>
    <div class="divider" style="top:146px"></div>
    <div class="comment" style="top:162px">Add comments</div>
    <div class="tools" style="top:165px">
      <svg viewBox="0 0 14 14" fill="none" stroke="var(--icon)" stroke-width="1.6"><path d="M6 8l2-2M5 6L3.5 7.5a2 2 0 003 3L8 9M9 8l1.5-1.5a2 2 0 00-3-3L6 5"/></svg>
      <svg viewBox="0 0 14 14" fill="none" stroke="var(--icon)" stroke-width="1.3"><circle cx="7" cy="7" r="5.5"/><path d="M4.5 8.2c1.2 1.6 3.8 1.6 5 0"/><circle cx="5.2" cy="5.5" r=".5" fill="var(--icon)"/><circle cx="8.8" cy="5.5" r=".5" fill="var(--icon)"/></svg>
    </div>
  </article>

  <article class="post" style="top:385px;height:485px">
    <div class="avatar" role="img" aria-label="Profile photo of Marisol"></div>
    <div class="author">Marisol</div>
    <div class="meta"><span>3 hours ago</span><span class="dot"></span><span>Message sent today lorium ipsum</span></div>
    <p class="body">After I put my dishes away, I will immediately wipe down the counter.</p>
    <div class="photo" role="img" aria-label="Photo of a woman wiping a kitchen counter beside a sink"></div>
    <div class="actions" style="left:34px;top:376px">
      <span class="action"><svg viewBox="0 0 20 20" fill="none" stroke="currentColor" stroke-width="1.3"><path d="M6 10V4a1 1 0 012 0v5M8 9V2.5a1 1 0 012 0V9M10 9V3a1 1 0 012 0v6M12 9V5a1 1 0 012 0v7c0 4-2 6-5 6s-4-1-6-5l-1-2a1 1 0 012-1l2 2"/></svg>250 high five</span>
      <span class="action"><svg viewBox="0 0 20 20" fill="none" stroke="currentColor" stroke-width="1.2"><rect x="2" y="3" width="16" height="11"/><path d="M5 6h10M5 8.5h10M5 11h7M12 14l2 3v-3"/></svg>85 Comments</span>
    </div>
    <div class="divider" style="top:432px"></div>
    <div class="comment" style="top:448px">Add comments</div>
    <div class="tools" style="top:451px">
      <svg viewBox="0 0 14 14" fill="none" stroke="var(--icon)" stroke-width="1.6"><path d="M6 8l2-2M5 6L3.5 7.5a2 2 0 003 3L8 9M9 8l1.5-1.5a2 2 0 00-3-3L6 5"/></svg>
      <svg viewBox="0 0 14 14" fill="none" stroke="var(--icon)" stroke-width="1.3"><circle cx="7" cy="7" r="5.5"/><path d="M4.5 8.2c1.2 1.6 3.8 1.6 5 0"/><circle cx="5.2" cy="5.5" r=".5" fill="var(--icon)"/><circle cx="8.8" cy="5.5" r=".5" fill="var(--icon)"/></svg>
    </div>
  </article>

  <article class="post" style="top:891px;height:199px">
    <div class="avatar light" role="img" aria-label="Profile photo of Tavia"></div>
    <div class="author">Tavia</div>
    <div class="meta"><span>3 hours ago</span><span class="dot"></span><span>Message sent today lorium ipsum</span></div>
    <p class="body">After I pour my morning cup of coffee, I will meditate for sixty seconds.</p>
    <div class="actions" style="left:129px;top:115px">
      <span class="action"><svg viewBox="0 0 20 20" fill="none" stroke="currentColor" stroke-width="1.3"><path d="M6 10V4a1 1 0 012 0v5M8 9V2.5a1 1 0 012 0V9M10 9V3a1 1 0 012 0v6M12 9V5a1 1 0 012 0v7c0 4-2 6-5 6s-4-1-6-5l-1-2a1 1 0 012-1l2 2"/></svg>250 high five</span>
      <span class="action"><svg viewBox="0 0 20 20" fill="none" stroke="currentColor" stroke-width="1.2"><rect x="2" y="3" width="16" height="11"/><path d="M5 6h10M5 8.5h10M5 11h7M12 14l2 3v-3"/></svg>85 Comments</span>
    </div>
    <div class="divider" style="top:146px"></div>
    <div class="comment" style="top:162px">Add comments</div>
    <div class="tools" style="top:165px">
      <svg viewBox="0 0 14 14" fill="none" stroke="var(--icon)" stroke-width="1.6"><path d="M6 8l2-2M5 6L3.5 7.5a2 2 0 003 3L8 9M9 8l1.5-1.5a2 2 0 00-3-3L6 5"/></svg>
      <svg viewBox="0 0 14 14" fill="none" stroke="var(--icon)" stroke-width="1.3"><circle cx="7" cy="7" r="5.5"/><path d="M4.5 8.2c1.2 1.6 3.8 1.6 5 0"/><circle cx="5.2" cy="5.5" r=".5" fill="var(--icon)"/><circle cx="8.8" cy="5.5" r=".5" fill="var(--icon)"/></svg>
    </div>
  </article>

  <footer class="footer">
    <div class="footer-text">
      <svg width="15" height="15" viewBox="0 0 16 16" fill="none" stroke="#222" stroke-width="1.8"><circle cx="8" cy="8" r="6.5"/><path d="M10.3 6.2a2.6 2.6 0 100 3.6"/></svg>
      <span>2018</span><span>|</span><span>www.ferrolanes.example</span>
    </div>
  </footer>
</body>
</html>
```